New cake shop needs a gorgeous website!

I need an easy to navigate and update (from my Mac - in layman's terms!) website for my new business - Crumb & Fern. This is a dietary friendly cake shop in Ponsonby, Auckland, New Zealand. We will be having Tarawhiti coffee (organic, fair-trade) Lumen Fizz range and specialty teas. Eat in, takeaway and delivery.
I will require you to upload and write if necessary, onto a program such as Pagecraft or similar.
I need a homepage, gallery page, price and ordering page (although the orders will be done via email/phone, no payments will be taken directly from the website) about us page, products and services page(this could incorporate the gallery maybe) a classes info page and a contact page.
My branding is very modern and clean. No vintage or french industrial is to be seen! We are sleek, with lots of white, black, charcoal grey and hot pink.
I will have photos to use in about 10 days, but I will upload some temporary images to start you off....
We also have a focus on 'a little bit good for you' and aim to make cakes that everyone can eat, whether they be gluten, dairy or egg intolerant or trying to lower the sugar in their diet.
A great design will be modern, exciting and convey a feel of luxury.
Please check out my pinterest page http://www.pinboardly.example/wrenbolt/coffee-cards-flyers-and-websites/
and feel free to use images from my instagram - fernbakenz.
Thanks!

```html
<!DOCTYPE html>
<html lang="en">
<head>
<meta charset="utf-8">
<title>Crumb &amp; Fern — Dietary Friendly Cake Shop</title>
<link rel="stylesheet" href="https://fonts.googleapis.com/css2?family=Open+Sans:wght@400;600;700&family=Dancing+Script:wght@400&display=swap">
<style>
  :root {
    --pink: #d9418b;
    --charcoal: #232123;
    --ink: #1f1f1f;
    --white: #ffffff;
    --paper: #efeeec;
    --muted: #9a989a;
    --line: #3a383a;
    --social-blue: #3c5a99;
    --text-grey: #555;
  }
  * { box-sizing: border-box; margin: 0; padding: 0; }
  html, body { width: 1200px; height: 2287px; overflow: hidden; background: var(--white); }
  body { position: relative; font-family: "Open Sans", Arial, sans-serif; color: var(--ink); }
  .abs { position: absolute; }

  /* Header */
  .site-header { left: 0; top: 0; width: 1200px; height: 99px; background: var(--white); }
  .brand { left: 162px; top: 30px; font-size: 34px; font-weight: 700; color: var(--pink); letter-spacing: 0.5px; white-space: nowrap; }
  .main-nav { left: 463px; top: 36px; display: flex; gap: 0; font-size: 11px; text-transform: uppercase; }
  .main-nav a { color: var(--ink); text-decoration: none; padding: 7px 13px; margin-right: 12px; }
  .main-nav a.active { background: var(--pink); color: var(--white); padding: 7px 14px; }

  /* Hero */
  .hero { left: 0; top: 99px; width: 1200px; height: 516px;
    background: radial-gradient(ellipse at 55% 40%, #8a3a3a 0%, #6b4a40 35%, #55504a 65%, #3a3633 100%); }
  .hero-shade { left: 0; top: 99px; width: 1200px; height: 516px; background: rgba(0,0,0,0.25); }
  .hero-title { left: 0; top: 290px; width: 1200px; text-align: center; color: var(--white); font-size: 37px; font-weight: 600; }
  .hero-sub { left: 0; top: 339px; width: 1200px; text-align: center; color: var(--white); font-size: 19px; }
  .hero-btn { left: 485px; top: 409px; width: 230px; height: 48px; border-radius: 24px; background: var(--white); color: var(--pink);
    font-size: 22px; font-weight: 600; text-align: center; line-height: 48px; }
  .hero-arrow { top: 324px; }

  /* Tiles */
  .tile { overflow: hidden; }
  .tile-menu { left: 0; top: 615px; width: 462px; height: 271px; background: var(--paper); }
  .tile-history { left: 737px; top: 615px; width: 463px; height: 271px; background: var(--pink); }
  .tile-recipes { left: 0; top: 886px; width: 737px; height: 271px; background: var(--charcoal); }
  .tile-social { left: 737px; top: 1157px; width: 274px; height: 273px; background: var(--social-blue); }
  .photo-cakepops { left: 462px; top: 615px; width: 275px; height: 271px; background: radial-gradient(circle at 40% 45%, #b27ac0, #6e3a7a 60%, #4a2a50); }
  .photo-flowers { left: 737px; top: 886px; width: 463px; height: 271px; background: radial-gradient(circle at 55% 55%, #e76a2a, #d4336a 45%, #f2e6ea 85%); }
  .photo-cats { left: 0; top: 1157px; width: 407px; height: 273px; background: linear-gradient(135deg, #b8a8a0, #7a5c8a 55%, #c8b8b0); }
  .photo-pops-bright { left: 407px; top: 1157px; width: 330px; height: 273px; background: radial-gradient(circle at 60% 40%, #e2a0c4, #c83a7a 45%, #e0b020 85%); }
  .photo-slice { left: 1011px; top: 1157px; width: 189px; height: 273px; background: linear-gradient(160deg, #f4f2f2 20%, #6a3a28 55%, #f0ecea 85%); }

  .kicker { font-family: "Dancing Script", cursive; font-size: 32px; line-height: 1; }
  .tile-heading { font-size: 32px; font-weight: 700; line-height: 1.05; text-transform: uppercase; }
  .tile-text { font-size: 14px; line-height: 1.5; }

  .menu-copy { right: 280px; top: 700px; text-align: right; }
  .menu-copy .kicker { color: var(--pink); }
  .menu-copy .tile-heading { color: var(--pink); }
  .menu-copy .tile-text { color: var(--pink); margin-top: 4px; }
  .history-copy { left: 783px; top: 700px; color: var(--white); }
  .history-copy .tile-text { margin-top: 4px; }
  .recipes-copy { right: 530px; top: 945px; text-align: right; color: var(--white); width: 480px; }
  .recipes-copy .tile-text { margin-top: 14px; font-size: 13.5px; }

  .social-mark { left: 849px; top: 1265px; width: 50px; height: 50px; border-radius: 50%; background: var(--white); }
  .social-label { left: 737px; top: 1350px; width: 274px; text-align: center; color: var(--white); font-size: 13px; }

  /* Events */
  .events-title { left: 0; top: 1500px; width: 1200px; text-align: center; font-size: 40px; font-weight: 600; }
  .event { top: 1598px; width: 290px; text-align: center; }
  .event-date { position: relative; width: 76px; height: 76px; margin: 0 auto; color: var(--white); font-size: 31px; font-weight: 600; line-height: 76px; }
  .event-date::after { content: ""; position: absolute; left: 28px; bottom: -10px; border-left: 10px solid transparent; border-right: 10px solid transparent; border-top: 10px solid; border-top-color: inherit; }
  .event-date.pink { background: var(--pink); border-top-color: var(--pink); }
  .event-date.dark { background: var(--charcoal); border-top-color: var(--charcoal); }
  .event-month { margin-top: 16px; color: var(--pink); font-size: 26px; }
  .event-head { margin-top: 10px; font-size: 15px; font-weight: 600; }
  .event-body { margin-top: 16px; font-size: 11px; line-height: 1.75; color: var(--text-grey); }
  .event-more { display: inline-block; margin-top: 28px; width: 74px; height: 31px; line-height: 31px; color: var(--white); font-size: 12px; }
  .event-more.pink { background: var(--pink); }
  .event-more.dark { background: var(--charcoal); }

  /* Footer */
  .site-footer { left: 0; top: 1955px; width: 1200px; height: 332px; background: var(--charcoal); }
  .footer-nav { left: 0; top: 2005px; width: 1200px; display: flex; justify-content: center; gap: 44px; font-size: 12px; color: var(--muted); }
  .footer-nav .active { color: var(--white); }
  .rule { left: 162px; width: 876px; height: 1px; background: var(--line); }
  .footer-label { top: 2102px; color: var(--white); font-size: 14px; }
  .social-square { top: 2132px; width: 34px; height: 34px; }
  .newsletter-input { left: 461px; top: 2132px; width: 173px; height: 34px; background: #2e2c2e; color: #777; font-size: 12px; line-height: 34px; padding-left: 16px; }
  .newsletter-btn { left: 634px; top: 2132px; width: 105px; height: 34px; background: var(--pink); color: var(--white); font-size: 14px; line-height: 34px; text-align: center; }
  .contact-lines { right: 161px; top: 2126px; text-align: right; color: var(--muted); font-size: 12px; line-height: 1.35; }
  .copyright { left: 0; top: 2233px; width: 1200px; text-align: center; color: #777; font-size: 11px; }
</style>
</head>
<body>

<header class="abs site-header">
  <div class="abs brand">Crumb &amp; Fern</div>
  <nav class="abs main-nav">
    <a class="active">Home</a><a>Menu</a><a>Blog</a><a>Events</a><a>Gallery</a><a>Reservations</a><a>Contact Us</a>
  </nav>
</header>

<section>
  <div class="abs hero" role="img" aria-label="Close-up photo of a cake topped with dried berries and yellow edible flowers"></div>
  <div class="abs hero-shade"></div>
  <h1 class="abs hero-title">WELCOME TO DIETARY FRIENDLY CAKE SHOP</h1>
  <p class="abs hero-sub">Lorem Ipsum is simply dummy text of the printing and typesetting.</p>
  <div class="abs hero-btn">MORE INFO</div>
  <svg class="abs hero-arrow" style="left:106px" width="26" height="52" viewBox="0 0 26 52"><polyline points="24,2 2,26 24,50" fill="none" stroke="#fff" stroke-width="2.5"/></svg>
  <svg class="abs hero-arrow" style="left:1070px" width="26" height="52" viewBox="0 0 26 52"><polyline points="2,2 24,26 2,50" fill="none" stroke="#fff" stroke-width="2.5"/></svg>
</section>

<section>
  <div class="abs tile tile-menu"></div>
  <div class="abs menu-copy">
    <div class="kicker">Discover</div>
    <div class="tile-heading">Our Menu</div>
    <div class="tile-text">Lorem Ipsum is simply dummy text.</div>
  </div>
  <div class="abs photo-cakepops" role="img" aria-label="Photo of purple cake pops with petals"></div>
  <div class="abs tile tile-history"></div>
  <div class="abs history-copy">
    <div class="kicker">Discover</div>
    <div class="tile-heading">Our Histery</div>
    <div class="tile-text">Lorem Ipsum is simply dummy text.</div>
  </div>

  <div class="abs tile tile-recipes"></div>
  <div class="abs recipes-copy">
    <div class="kicker">Tasteful</div>
    <div class="tile-heading">Recipes</div>
    <div class="tile-text">Lorem Ipsum is simply dummy text of the printing and typeset<br>ing industry. Lorem Ipsum has been the industry's standard dummy text<br>ever since the 1500s, when an unknown printer took a galley</div>
  </div>
  <div class="abs photo-flowers" role="img" aria-label="Photo of colourful edible pansies on a cake"></div>

  <div class="abs photo-cats" role="img" aria-label="Photo of cats resting in a wicker basket"></div>
  <div class="abs photo-pops-bright" role="img" aria-label="Photo of pink cake pops among bright flowers"></div>
  <div class="abs tile tile-social"></div>
  <div class="abs social-mark"></div>
  <div class="abs social-label">Like Now !</div>
  <div class="abs photo-slice" role="img" aria-label="Photo of a sliced chocolate layer cake"></div>
</section>

<section>
  <h2 class="abs events-title">OUR EVENTS</h2>
  <article class="abs event" style="left:155px">
    <div class="event-date pink">18</div>
    <div class="event-month">October</div>
    <div class="event-head">Lorem Ipsum is simply</div>
    <p class="event-body">Lorem Ipsum is simply dummy text of the print-<br>ing and typesetting industry. Lorem Ipsum has<br>been the industry's standard unchanged</p>
    <span class="event-more pink">MORE</span>
  </article>
  <article class="abs event" style="left:455px">
    <div class="event-date dark">22</div>
    <div class="event-month">October</div>
    <div class="event-head" style="font-weight:400">Lorem Ipsum is simply</div>
    <p class="event-body">Lorem Ipsum is simply dummy text of the print-<br>ing and typesetting industry. Lorem Ipsum has<br>been the industry's standard unchanged</p>
    <span class="event-more dark">MORE</span>
  </article>
  <article class="abs event" style="left:755px">
    <div class="event-date dark">28</div>
    <div class="event-month">October</div>
    <div class="event-head" style="font-weight:400">Lorem Ipsum is simply</div>
    <p class="event-body">Lorem Ipsum is simply dummy text of the print-<br>ing and typesetting industry. Lorem Ipsum has<br>been the industry's standard unchanged</p>
    <span class="event-more dark">MORE</span>
  </article>
</section>

<footer>
  <div class="abs site-footer"></div>
  <nav class="abs footer-nav">
    <span class="active">Home</span><span>Menu</span><span>Blog</span><span>Events</span><span>Gallery</span><span>Reservations</span><span>Contact Us</span>
  </nav>
  <div class="abs rule" style="top:2068px"></div>
  <div class="abs footer-label" style="left:166px">Follow Us</div>
  <div class="abs social-square" style="left:162px;background:#4a4850"></div>
  <div class="abs social-square" style="left:204px;background:#4a4850"></div>
  <div class="abs social-square" style="left:246px;background:#4a4850"></div>
  <div class="abs footer-label" style="left:467px">News letter</div>
  <div class="abs newsletter-input">Enter your email</div>
  <div class="abs newsletter-btn">Subscribe</div>
  <div class="abs footer-label" style="right:165px">Contact Us</div>
  <div class="abs contact-lines">Address<br>New Street<br>ph :&nbsp; 123 456 7890</div>
  <div class="abs rule" style="top:2202px"></div>
  <div class="abs copyright">Crumb &amp; Fern 2014 Allright Reserved</div>
</footer>

</body>
</html>
```